OWNERS HANDBOOK

Take a MICROSOFT WORD document and turn it into a nicely designed and structured PDF or similar to circulate to Owners and to make available online for Owners to access.

```html
<!DOCTYPE html>
<html lang="en">
<head>
<meta charset="utf-8">
<title>Monte Verde Village – Owner Handbook 2023</title>
<link href="https://fonts.googleapis.com/css2?family=PT+Sans+Narrow:wght@400;700&display=swap" rel="stylesheet">
<style>
:root{
  --green:#5aa83a;
  --green-light:#a9d46c;
  --blue:#1f4f9c;
  --text:#2b2b2b;
  --magenta:#e2007a;
  --paper:#ffffff;
  --frame:#9fcf75;
}
*{box-sizing:border-box;margin:0;padding:0}
html,body{width:1200px;height:414px;overflow:hidden;background:#fff}
body{position:relative;font-family:"PT Sans Narrow",sans-serif;color:var(--text)}
.page{position:absolute;top:14px;width:271px;height:383px;background:var(--paper);border:1px solid var(--frame);overflow:hidden}
.p13{left:10px}.p14{left:302px}.p15{left:600px}.p16{left:913px}
.masthead{position:relative;height:55px;background:linear-gradient(90deg,#5fae3e 0%,#7fb556 45%,#9bb58a 70%,#b6c4b4 100%)}
.masthead .title{position:absolute;left:19px;top:17px;color:#fff;font-weight:700;font-size:10.3px;letter-spacing:.1px;white-space:nowrap}
.masthead .sub{position:absolute;left:19px;top:34px;color:#fff;font-weight:700;font-size:6px}
.content{position:absolute;left:19px;right:19px;top:64px}
h2{display:flex;align-items:center;gap:3px;color:var(--blue);font-size:6.6px;font-weight:700;margin:4px 0 2px -1px;line-height:8px}
.ico{width:8px;height:8px;flex:none}
p{font-size:4.85px;line-height:6.5px;margin:0 0 2.5px 3px}
.list{list-style:none;margin:0 0 1px 0}
.list li{display:flex;font-size:4.85px;line-height:6.3px;padding:1.2px 0;border-bottom:.5px solid #c9c9c9}
.list li::before{content:"";width:3.5px;height:3.5px;background:var(--blue);margin:1.4px 5px 0 0;flex:none}
.list .n{width:55px}
.alert{color:var(--magenta);font-size:5px;line-height:6.5px;margin:0 0 2.5px 0}
.footer{position:absolute;left:0;right:0;bottom:0;height:13px;background:linear-gradient(90deg,#fff 45%,var(--green-light) 100%)}
.footer .num{position:absolute;left:250px;top:0;width:20px;height:13px;background:var(--green);color:#fff;font-size:5px;padding:2px 0 0 4px}
.appx{display:flex;align-items:center;gap:3px;margin:0 0 4px 0;border-bottom:.8px solid var(--green);padding-bottom:1px}
.appx .badge{width:18px;height:18px;background:var(--green);flex:none;margin-bottom:-6px}
.appx h1{color:var(--blue);font-size:11px;font-weight:700;letter-spacing:.1px}
h3{color:var(--blue);font-size:6.3px;font-weight:700;margin:4px 0 2px 0}
.p15 p{margin-left:0;text-indent:3px}
.evac{position:absolute;left:20px;width:230px;background:var(--green);padding:2px}
.evac .cap{color:#fff;font-weight:700;font-size:6px;text-align:center;line-height:9px}
.evac .map{background:#f3f6f1;margin:1px 2px}
.evac .band{color:#fff;font-weight:700;font-size:4.2px;text-align:center;line-height:5px}
.evac .guide{display:flex;gap:1px;margin:0 2px 2px}
.evac .guide div{flex:1;background:#fafafa}
</style>
</head>
<body>

<section class="page p13">
  <header class="masthead" role="img" aria-label="Photo of palm-lined resort avenue under a green tint">
    <div class="title">MONTE VERDE VILLAGE AND OLIVE TERRACES</div>
    <div class="sub">OWNER HANDBOOK 2023</div>
  </header>
  <div class="content">
    <h2><svg class="ico" viewBox="0 0 10 10"><path d="M2 5h6v2a3 3 0 0 1-6 0z" fill="#4a90c8"/><ellipse cx="5" cy="3" rx="2" ry="1" fill="none" stroke="#5aa83a" stroke-width=".8"/></svg>Café’s within the resort</h2>
    <ul class="list">
      <li><span class="n">Monte Verde Café</span>+351 900 100 211 (dine in and takeaway service available)</li>
      <li><span class="n">Café da Praça</span>+351 900 100 322 (dine in and takeaway service available)</li>
    </ul>
    <h2><svg class="ico" viewBox="0 0 10 10"><path d="M1 2h2l1 5h5l1-4H3.5" fill="none" stroke="#5aa83a" stroke-width="1"/><circle cx="4.5" cy="8.5" r=".9" fill="#1f4f9c"/><circle cx="8" cy="8.5" r=".9" fill="#1f4f9c"/></svg>Supermarket</h2>
    <p>We have a small supermarket Mercado Sol within the resort (next to the Monte Verde Café)</p>
    <h2><svg class="ico" viewBox="0 0 10 10"><circle cx="5" cy="5" r="4" fill="none" stroke="#5aa83a" stroke-width="1"/><path d="M3 6l2-3 2 3" fill="none" stroke="#1f4f9c" stroke-width=".8"/></svg>Hairdressers within the complex:</h2>
    <ul class="list">
      <li><span class="n">Hair and Beauty Salon</span>+351 900 100 433</li>
      <li><span class="n">Salon Amélie</span>+351 900 100 544</li>
    </ul>
    <h2><svg class="ico" viewBox="0 0 10 10"><path d="M4 9V1l4 2-4 2" fill="#5aa83a"/><path d="M1 9h8" stroke="#5aa83a"/></svg>Oliveira Hotel and Golf Course</h2>
    <p>A short drive and not too far walk away is the Oliveira Monte Verde Hotel and Golf club.</p>
    <p>Monte Verde Owners receive a discount for golf at the club and please ensure you show the reception desk your Monte Verde Owners card with up-to-date year label on the card. Please note the Owners card is available from Customer Service Offices at Horizon Living office (beside Barrel Pub).</p>
    <h2><svg class="ico" viewBox="0 0 10 10"><circle cx="5" cy="5" r="4.2" fill="none" stroke="#5aa83a" stroke-width="1"/><circle cx="5" cy="5" r="1.6" fill="#1f4f9c"/></svg>Communal WIFI</h2>
    <p>A communal WIFI service is provided in the Terraces Area next to the main pool Area for all Owners and their guest to use.</p>
    <p>Username and Passwords are updated regularly, and full details can be obtained from staff working in the Bar area of the Terraces.</p>
    <h2><svg class="ico" viewBox="0 0 10 10"><path d="M2 2h6l-1 7H3z" fill="#1f4f9c"/></svg>Waste Disposal</h2>
    <p>Owners are responsible for the proper use of the Condominium waste disposal bins strategically placed near each apartment block by the Waste disposal company Limpamar.</p>
    <p>Please remember to ensure you separate Plastics and glass from the general waste you are disposing.</p>
    <h2><svg class="ico" viewBox="0 0 10 10"><rect x="1" y="3" width="8" height="5" fill="#5aa83a" transform="rotate(-12 5 5)"/></svg>Cash Machines (ATM)</h2>
    <p>There are 2 ATM machines in our area, one is beside Barrel pub and the other one in between the Bistro and the Supermarket.</p>
    <h2><svg class="ico" viewBox="0 0 10 10"><rect x="1" y="1" width="8" height="8" fill="#1f4f9c"/><path d="M5 2v6M2 5h6" stroke="#fff" stroke-width="1"/></svg>Air Conditioning</h2>
    <p>The majority if not all the Apartments are using A/C within the apartment. It is advisable to have your respective A/C units and chiller serviced on a regular basis. There are quite a few local A/C maintenance service providers, including:</p>
    <ul class="list">
      <li><span class="n">Clima Pro -</span>+351 289 000 655</li>
      <li><span class="n">Frio Norte -</span>+351 289 000 766</li>
    </ul>
  </div>
  <footer class="footer"><span class="num">13</span></footer>
</section>

<section class="page p14">
  <header class="masthead" role="img" aria-label="Photo of palm-lined resort avenue under a green tint">
    <div class="title">MONTE VERDE VILLAGE AND OLIVE TERRACES</div>
    <div class="sub">OWNER HANDBOOK 2023</div>
  </header>
  <div class="content">
    <h2><svg class="ico" viewBox="0 0 10 10"><rect x="1" y="1" width="8" height="8" fill="#1f4f9c"/><path d="M6 2L3.5 5.5h2L4 8.5" fill="none" stroke="#fff" stroke-width=".9"/></svg>Electricity Supply</h2>
    <p>In many parts of the southern coast, intermittent and disrupted electrical supply can occur, this may require in some instances for the Owner to call Security. Access to the Services cupboard on the ground floor in each block, (where the individual electricity meters are located) is through the key provided to each apartment or alternatively by contacting Security who can open the services doors.</p>
    <h2><svg class="ico" viewBox="0 0 10 10"><path d="M1 5l4-4 4 4v4H1z" fill="#1f4f9c"/><circle cx="5" cy="6" r="1.3" fill="#fff"/></svg>Apartment Alarms</h2>
    <p>A number of apartments have alarms connected to the Guarda Norte security centre situated in the security office opposite the Ember restaurant and near to 80 block.</p>
    <p>If you are leaving your apartment for any period of time, we strongly recommend you advise the Property Management company – Customer Services and advise them if your alarm is on.</p>
    <h2><svg class="ico" viewBox="0 0 10 10"><circle cx="5" cy="5" r="3.2" fill="none" stroke="#5aa83a" stroke-width="2" stroke-dasharray="1.5 1"/></svg>Pool and Gardens Maintenance</h2>
    <p>The Gardens and Pool maintenance is outsourced to a local company who are responsible for the upkeep of every aspect of the Gardens and Pools and similarly in all common areas surrounding and attached to our complex.</p>
    <p>Throughout the year you will hear and see the gardening or Pool staff at work, keeping our Gardens beautiful.</p>
    <h2><svg class="ico" viewBox="0 0 10 10"><circle cx="5" cy="5" r="4.2" fill="#5aa83a"/><path d="M2.2 7.8l5.6-5.6" stroke="#fff" stroke-width="1.1"/></svg>Pest control</h2>
    <p>We have continual Pest Control programme in place and in particular for dealing with the processionary caterpillars that become evident in the early spring of each year. If you see a procession near your apartment block or in the Gardens area, PLEASE ALERT THE PROPERTY MANAGEMENT COMPANY ASAP!</p>
    <h2><svg class="ico" viewBox="0 0 10 10"><circle cx="5" cy="5" r="4.2" fill="none" stroke="#5aa83a" stroke-width="1"/><path d="M5 2c2 2 1.5 3 1.5 4a1.5 1.5 0 0 1-3 0c0-1 .5-2 1.5-4z" fill="#1f4f9c"/></svg>Fire Safety</h2>
    <p class="alert">SHOULD YOU DETECT A FIRE IN YOUR APARTMENT, BLOCK, COMMON AREAS OR GARDENS ALERT SECURITY AND PLEASE CALL 112 FOR THE BOMBEIROS WHO WILL ARRIVE TO DEAL WITH THE ISSUE.</p>
    <p>FULL FIRE EVACUATION PROCEDURES ARE CONTAINED WITHIN APPENDIX 2 OF THIS HANDBOOK.</p>
    <h2><svg class="ico" viewBox="0 0 10 10"><rect x="2" y="1" width="6" height="7" rx="1" fill="#1f4f9c"/><rect x="3" y="2" width="4" height="2.5" fill="#fff"/></svg>Public Transport</h2>
    <p>Public buses run on the N518 main road adjoining the entrance to Monte Verde, bus stops are on both sides of the N518 (the main road outside the complex).</p>
    <p>Trains are available and nearest stations are at Portela, Valmar and Santa Luz.</p>
  </div>
  <footer class="footer"><span class="num">14</span></footer>
</section>

<section class="page p15">
  <header class="masthead" role="img" aria-label="Photo of palm-lined resort avenue under a green tint">
    <div class="title">MONTE VERDE VILLAGE AND OLIVE TERRACES</div>
    <div class="sub">OWNER HANDBOOK 2023</div>
  </header>
  <div class="content" style="top:67px">
    <div class="appx">
      <svg class="badge" viewBox="0 0 18 18"><rect width="18" height="18" fill="#5aa83a"/><g fill="#fff"><circle cx="4" cy="7" r="1.2"/><circle cx="7.3" cy="7" r="1.2"/><circle cx="10.6" cy="7" r="1.2"/><circle cx="14" cy="7" r="1.2"/><rect x="3" y="9" width="2" height="5"/><rect x="6.3" y="9" width="2" height="5"/><rect x="9.6" y="9" width="2" height="5"/><rect x="13" y="9" width="2" height="5"/></g></svg>
      <h1>APPENDIX 1 – PEAK SEASON PROCEDURES</h1>
    </div>
    <h3>Peak Season procedure for visitors to Olive Terraces Club (OTC)</h3>
    <p>The High Season Procedure (HSP) will be triggered when necessary whenever the volume and demand for sunbeds is high. An Email will be sent to owners informing them when the procedure will commence. When the HSP is activated then sunbeds will be allocated by the pool attendants when shown the sunbed tokens.</p>
    <p>Please do not use towels or other personal items in order to “reserve sunbeds”. These will be removed by the Pool Attendant.</p>
    <h3>Pool Attendants</h3>
    <p>During the summer months from July to September there will be pool attendants to assist with any queries or issues and also to manage the sunbed allocation when necessary.</p>
    <p>At the peak period there will be two pool attendants every day, one of whom will be at the Pool Attendant post at the Central pool at all times from the hours of 10:00 to 19:00.</p>
    <p>Pool attendants are also instructed to remove towels etc. from unoccupied sunbeds. If you do find your towels have been removed, then please go to the pool attendant who will return them to you.</p>
    <h3>Sunbed tokens</h3>
    <p>All Apartments will be provided with Sunbed tokens. These will need to be shown to the Pool Attendants if and when the High Season Procedure (HSP) is triggered.</p>
    <p>The tokens can be collected from customer services. (5 for 2-bedroom and 7 for 3-bedroom apartments)</p>
    <p>If tokens are lost, then please report it to customer services and replacements can be provided at a cost of 2 Euros per token.</p>
    <h3>North Pool</h3>
    <p>The North pool (near to B14 and B15) has been designated as a swimming only pool. Inflatables are therefore not permitted at this pool at any time.</p>
    <h3>Inflatables</h3>
    <p>Inflatables are permitted in the central and lower pools. We do however ask that you respect other visitors when using them in and around the pool areas. Inflatables should be removed from the pool when not in use.</p>
    <h3>Queries or Complaints</h3>
    <p>In the first instance please report any concerns to the Pool Attendant. If not resolved, then ring the VGM Help number 289 000 411.</p>
    <p>IMPORTANT NOTE: abuse of the pool attendants is unacceptable. They have been instructed to report any abuse to security and VGM.</p>
  </div>
  <footer class="footer"><span class="num">15</span></footer>
</section>

<section class="page p16">
  <header class="masthead" role="img" aria-label="Photo of palm-lined resort avenue under a green tint">
    <div class="title">MONTE VERDE VILLAGE AND OLIVE TERRACES</div>
    <div class="sub">OWNER HANDBOOK 2023</div>
  </header>
  <div class="content" style="top:67px">
    <div class="appx">
      <svg class="badge" viewBox="0 0 18 18"><rect width="18" height="18" fill="#5aa83a"/><path d="M4 9h6V5l5 4-5 4V9" fill="#fff"/><path d="M6 4c2 2 1.5 3.5 1.5 5a1.5 1.5 0 0 1-3 0c0-1.5.5-3 1.5-5z" fill="#1f4f9c"/></svg>
      <h1>APPENDIX 2 – FIRE EVACUATION PROCEDURES</h1>
    </div>
  </div>
  <div class="evac" style="top:89px;height:139px">
    <div class="cap">PLANTA DE EMERGÊNCIA - PLAN D’ÉVACUATION - EVACUATION MAP</div>
    <div class="map" role="img" aria-label="Evacuation floor plan of the upper resort blocks with escape routes" style="height:75px"></div>
    <div class="band">EM CASO DE INCÊNDIO - EN CAS D’INCENDIE - IN CASE OF FIRE</div>
    <div class="guide" role="img" aria-label="Fire instructions in Portuguese, French and English with legend" style="height:41px"><div></div><div></div><div></div><div></div></div>
  </div>
  <div class="evac" style="top:233px;height:135px">
    <div class="cap">PLANTA DE EMERGÊNCIA - PLAN D’ÉVACUATION - EVACUATION MAP</div>
    <div class="map" role="img" aria-label="Evacuation floor plan of the lower resort blocks with escape routes" style="height:70px"></div>
    <div class="band">EM CASO DE INCÊNDIO - EN CAS D’INCENDIE - IN CASE OF FIRE</div>
    <div class="guide" role="img" aria-label="Fire instructions in Portuguese, French and English with legend" style="height:42px"><div></div><div></div><div></div><div></div></div>
  </div>
  <footer class="footer"><span class="num">16</span></footer>
</section>

</body>
</html>
```